Design a menu for a Pizza company

I need help designing a color menu for a pizza company. It will be a 9x16" trifold menu (3-panel). I would like to include some photos of pizza, salads, subs, sandwiches, drinks, etc. (no clipart). Attached is an example of an existing menu. I need to make the menu full color. We would like to modernize this menu with full color photos like the attached sample menu. The final files should have editable files so I can edit prices and menu items as needed. I prefer CorelDraw graphics software.

Target Market(s)

General public.

Industry/Entity Type

Restaurant

Font styles to use
Sans Serif

Colors
ec1f27
fffefc
9bcb3b

Requirements
Must have
• Must have photos and editable fonts. I will need to be able to edit the contents of the menu after you provide me with the final files.
Nice to have
• It would be nice to have this menu created in CorelDraw X7 or X8.
Should not have
• Should not have clip art or low resolution photos.

```html
<!DOCTYPE html>
<html lang="en">
<head>
<meta charset="utf-8">
<title>Pizza Restaurant – Trifold Menu</title>
<link href="https://fonts.googleapis.com/css2?family=Oswald:wght@500;600&family=Roboto+Condensed:ital,wght@0,400;0,700;1,400&display=swap" rel="stylesheet">
<style>
  :root{
    --red:#ec1f27;
    --paper:#fffefc;
    --green:#9bcb3b;
    --yellow:#f5e614;
    --ink:#1d1d1b;
    --backdrop:#5b3a12;
    --panel-a:#f6f8c8;
    --panel-b:#e3f0a6;
  }
  *{box-sizing:border-box;margin:0;padding:0}
  html,body{width:1200px;height:1200px;overflow:hidden}
  body{background:var(--backdrop);font-family:"Roboto Condensed",sans-serif;color:var(--ink);position:relative}

  /* ---------- Cover ---------- */
  .cover{position:absolute;left:455px;top:15px;width:290px;height:490px;background:var(--red);overflow:hidden;box-shadow:0 8px 20px rgba(0,0,0,.45)}
  .cover__name{position:absolute;left:22px;top:26px;width:250px;font-family:"Oswald",sans-serif;font-weight:600;font-size:34px;line-height:1.05;color:var(--yellow)}
  .cover__art{position:absolute;left:40px;top:120px;width:220px;height:250px;border-radius:10px;background:radial-gradient(circle at 50% 45%,#ffffff 0%,#f3d6d6 45%,#d51c24 100%)}
  .cover__band{position:absolute;left:0;bottom:0;width:100%;height:112px;background:var(--green);padding:12px 16px;font-family:"Oswald",sans-serif;color:var(--paper)}
  .cover__hours{font-size:12px;line-height:1.45;letter-spacing:.02em}
  .cover__cards{font-size:12px;color:var(--yellow);margin-top:2px}
  .cover__carry{position:absolute;right:16px;bottom:8px;font-size:24px;font-weight:600;color:var(--yellow)}

  /* ---------- Inside spread ---------- */
  .spread{position:absolute;left:30px;top:522px;width:1140px;height:660px;display:flex;box-shadow:0 10px 24px rgba(0,0,0,.5)}
  .panel{width:380px;height:100%;padding:10px 24px 10px;background:radial-gradient(ellipse at 55% 40%,var(--panel-a) 0%,var(--panel-b) 80%);position:relative}
  .panel + .panel{border-left:1px solid rgba(0,0,0,.08)}

  .heading{font-family:"Oswald",sans-serif;font-weight:600;font-size:16px;color:var(--red);text-align:center;line-height:20px;margin:2px 0 2px;position:relative}
  .heading::before{content:"";position:absolute;left:12%;right:12%;top:4px;height:4px;background:linear-gradient(90deg,transparent,rgba(236,31,39,.35),transparent)}
  .heading::after{content:"";position:absolute;left:6%;right:6%;bottom:0;height:2px;background:linear-gradient(90deg,transparent,var(--red),transparent)}

  .note{font-size:10px;font-style:italic;text-align:center;line-height:13px;margin:2px 0 3px}

  .row{display:flex;align-items:baseline;font-size:12px;line-height:20px;white-space:nowrap}
  .row b{font-weight:700}
  .row i{font-size:9.5px;margin-left:3px}
  .lead{flex:1;border-bottom:1px dotted var(--ink);margin:0 4px;transform:translateY(-3px);min-width:6px}
  .price{font-weight:700;width:32px;text-align:right}

  .tight .row{line-height:16px}
  .mid .row{line-height:17px}

  .two-col{display:flex;gap:8px;align-items:center}
  .two-col .list{width:190px}
  .photo{border-radius:10px}

  .apps-photo{position:absolute;left:6px;top:6px;width:54px;height:30px;border-radius:8px;background:linear-gradient(135deg,#e9a948,#c46b1d)}
  .sides-photo{width:130px;height:100px;background:radial-gradient(circle at 40% 50%,#f1b347,#d7731e 70%,transparent 72%)}
  .salad-photo{width:140px;height:110px;background:radial-gradient(ellipse at 50% 55%,#cfdba0 0%,#7a9c3a 55%,transparent 72%)}
  .grill-photo{width:150px;height:120px;background:radial-gradient(ellipse at 50% 55%,#f4d27a 0%,#e29a36 50%,transparent 72%)}

  .footnote{font-size:11px;font-style:italic;text-align:center;line-height:14px;margin-top:4px}

  /* sub price columns */
  .sizes{display:flex;justify-content:flex-end;gap:14px;height:14px}
  .badge{width:18px;height:14px;border-radius:7px;background:var(--red);color:var(--paper);font-family:"Oswald",sans-serif;font-size:9px;line-height:14px;text-align:center}
  .subs .row .price + .price{margin-left:14px}

  /* pizza grid */
  .pz-head,.pz{display:grid;grid-template-columns:1fr 34px 38px 40px 42px;align-items:baseline;font-size:12px;line-height:17px}
  .pz-head span{background:var(--red);color:var(--paper);font-family:"Oswald",sans-serif;font-size:10px;line-height:13px;text-align:center;margin:0 1px}
  .pz-head .blank{background:none}
  .pz .n{display:flex;align-items:baseline;white-space:nowrap;min-width:0}
  .pz .n b{font-weight:700}
  .pz .n i{font-size:9.5px;margin-left:3px}
  .pz--wide .n{grid-column:1 / span 2}
  .pz span:not(.n):not(.lead){font-weight:700;text-align:right}
  .pz-note{font-size:9.5px;font-style:italic;line-height:11px;margin:-2px 0 2px}
</style>
</head>
<body>

<section class="cover">
  <div class="cover__name">Pizza Restaurant</div>
  <div class="cover__art" role="img" aria-label="Illustration of a chef tossing pizza dough"></div>
  <div class="cover__band">
    <div class="cover__hours">MON - THURSDAY | 10:30 A.M. - 9:30 P.M.<br>FRI - SATURDAY | 10:30 A.M. - 10:00 P.M.<br>SUNDAY | NOON - 8:00 P.M.</div>
    <div class="cover__cards">All Major Cards Accepted</div>
    <div class="cover__carry">CARRY OUT</div>
  </div>
</section>

<main class="spread">
  <!-- Left panel -->
  <section class="panel">
    <div class="apps-photo" role="img" aria-label="Photo of mozzarella sticks with tomato"></div>
    <h2 class="heading">APPETIZERS</h2>
    <div class="row"><b>Mozzarella Sticks</b><i>served w/Marinara sauce</i><span class="lead"></span><span class="price">6.49</span></div>
    <div class="row"><b>Chicken Tenders</b><i>served w/Honey Mustard sauce</i><span class="lead"></span><span class="price">6.49</span></div>
    <div class="row"><b>Jalapeno Peppers</b><i>served w/Marinara sauce</i><span class="lead"></span><span class="price">6.49</span></div>
    <div class="row"><b>8 Piece Buffalo Wings</b><i>served w/ Blue Cheese sauce</i><span class="lead"></span><span class="price">6.49</span></div>
    <div class="row"><b>Fried Mushroom</b><i>served w/ Ranch Dressing</i><span class="lead"></span><span class="price">6.49</span></div>

    <h2 class="heading">SIDE ORDERS</h2>
    <div class="two-col">
      <div class="list">
        <div class="row"><b>French Fries</b><span class="lead"></span><span class="price">2.49</span></div>
        <div class="row"><b>Onion Rings</b><span class="lead"></span><span class="price">2.49</span></div>
        <div class="row"><b>Garlic Bread</b><span class="lead"></span><span class="price">1.99</span></div>
        <div class="row"><b>Garlic Bread w/ Cheese</b><span class="lead"></span><span class="price">2.99</span></div>
        <div class="row"><b>Cole Slaw</b><span class="lead"></span><span class="price">1.99</span></div>
      </div>
      <div class="photo sides-photo" role="img" aria-label="Photo of onion rings and french fries"></div>
    </div>

    <h2 class="heading">GARDEN FRESH SALADS</h2>
    <p class="note">Choice of Dressing :<br>Ranch, French, Italian, Blue Cheese, Thousand Island</p>
    <div class="row"><b>Garden Salad</b><span class="lead"></span><span class="price">4.49</span></div>
    <div class="row"><b>Chef Salad</b><i>(ham, salami, cheese &amp; hard boiled egg)</i><span class="lead"></span><span class="price">7.99</span></div>
    <div class="row"><b>Greek Salad</b><span class="lead"></span><span class="price">7.99</span></div>
    <div class="row"><b>Grilled Chicken Salad</b><i>(w/ cheese &amp; hard boiled egg)</i><span class="lead"></span><span class="price">7.99</span></div>
    <div class="row"><b>Gyro Salad (Beef or Chicken)</b><span class="lead"></span><span class="price">7.99</span></div>
    <div class="row"><b>Tuna Salad</b><span class="lead"></span><span class="price">7.99</span></div>

    <h2 class="heading">SANDWICHES</h2>
    <p class="note">All Available on Wheat, Rye, White Bread</p>
    <div class="two-col">
      <div class="list">
        <div class="row"><b>Ham &amp; Cheese w/ LTM</b><span class="lead"></span><span class="price">5.99</span></div>
        <div class="row"><b>Roast Beef w/ LTM</b><span class="lead"></span><span class="price">5.99</span></div>
        <div class="row"><b>Tuna Salad w/ LTM</b><span class="lead"></span><span class="price">5.99</span></div>
        <div class="row"><b>Turkey, Ham, Cheese w/ LTM</b><span class="lead"></span><span class="price">5.99</span></div>
        <div class="row"><b>Turkey &amp; Cheese w/ LTM</b><span class="lead"></span><span class="price">5.99</span></div>
      </div>
      <div class="photo salad-photo" role="img" aria-label="Photo of tuna salad served in an avocado half"></div>
    </div>
    <p class="footnote">* "Consuming raw or undercooked meats may increase<br>your risk of foodborne illness."</p>
  </section>

  <!-- Middle panel -->
  <section class="panel subs tight">
    <h2 class="heading">SUPER SUBS</h2>
    <div class="sizes"><span class="badge">8"</span><span class="badge">12"</span></div>
    <div class="row"><b>Italian Cold Cut</b><i>(ham, salami, cheese, LT, onion, HP, OV)</i><span class="lead"></span><span class="price">6.99</span><span class="price">9.99</span></div>
    <div class="row"><b>American Hero</b><i>(turkey, roast beef, American cheese, LTM)</i><span class="lead"></span><span class="price">6.99</span><span class="price">9.99</span></div>
    <div class="row"><b>Virginia Cold Cut</b><i>(ham, turkey, cheese, LTM)</i><span class="lead"></span><span class="price">6.99</span><span class="price">9.99</span></div>
    <div class="row"><b>Tuna Salad</b><i>(w/LTM)</i><span class="lead"></span><span class="price">6.99</span><span class="price">9.99</span></div>
    <div class="row"><b>Ham &amp; Cheese</b><i>(w/LTM)</i><span class="lead"></span><span class="price">6.99</span><span class="price">9.99</span></div>
    <div class="row"><b>Turkey Sub</b><i>(w/LTM)</i><span class="lead"></span><span class="price">6.99</span><span class="price">9.99</span></div>
    <div class="row"><b>Club Sub</b><i>(turkey, ham, bacon, LTM)</i><span class="lead"></span><span class="price">6.99</span><span class="price">9.99</span></div>
    <div class="row"><b>Roast Beef</b><i>(w/LTM)</i><span class="lead"></span><span class="price">6.99</span><span class="price">9.99</span></div>

    <h2 class="heading">HOT SUBS</h2>
    <div class="sizes"><span class="badge">8"</span><span class="badge">12"</span></div>
    <div class="row"><b>Steak &amp; Cheese</b><i>(w/ grilled onion, LTM)</i><span class="lead"></span><span class="price">6.99</span><span class="price">9.99</span></div>
    <div class="row"><b>Steak &amp; Mushroom</b><i>(w/ grilled onion, LTM)</i><span class="lead"></span><span class="price">6.99</span><span class="price">9.99</span></div>
    <div class="row"><b>Steak</b><i>(w/ green peppers, grilled onion, LTM)</i><span class="lead"></span><span class="price">6.99</span><span class="price">9.99</span></div>
    <div class="row"><b>Steak</b><i>(w/ onions, pizza sauce)</i><span class="lead"></span><span class="price">6.99</span><span class="price">9.99</span></div>
    <div class="row"><b>Billy Dooley</b><i>(w/ steak, grilled onion, green peppers, egg, LTM)</i><span class="lead"></span><span class="price">6.99</span><span class="price">9.99</span></div>
    <div class="row"><b>Tom Dooley</b><i>(w/ ham, hamburger, egg, LTM)</i><span class="lead"></span><span class="price">6.99</span><span class="price">9.99</span></div>
    <div class="row"><b>Hot Sam</b><i>(w/ham, bacon, egg, LTM)</i><span class="lead"></span><span class="price">6.99</span><span class="price">9.99</span></div>
    <div class="row"><b>*Cheeseburger Sub</b><i>(w/LTM)</i><span class="lead"></span><span class="price">6.99</span><span class="price">9.99</span></div>
    <div class="row"><b>Pastrami</b><i>(warm)</i><span class="lead"></span><span class="price">6.99</span><span class="price">9.99</span></div>
    <div class="row"><b>Veggie Sub</b><i>(LT, olive, green pepper, onion, mushroom, LTM)</i><span class="lead"></span><span class="price">6.99</span><span class="price">9.99</span></div>
    <div class="row"><b>B.L.T.</b><i>(w/ mayonnaise)</i><span class="lead"></span><span class="price">6.99</span><span class="price">9.99</span></div>
    <div class="row"><b>Crab Cake</b><i>(w/LTM)</i><span class="lead"></span><span class="price">6.99</span><span class="price">9.99</span></div>
    <div class="row"><b>Fish Filet</b><i>(w/ow)</i><span class="lead"></span><span class="price">6.99</span><span class="price">9.99</span></div>
    <div class="row"><b>Chicken Filet</b><i>(w/LTM)</i><span class="lead"></span><span class="price">6.99</span><span class="price">9.99</span></div>

    <h2 class="heading">PARMIGIANA SUBS</h2>
    <div class="sizes"><span class="badge">8"</span><span class="badge">12"</span></div>
    <div class="row"><b>Meatball Parmigiana</b><span class="lead"></span><span class="price">6.99</span><span class="price">9.99</span></div>
    <div class="row"><b>Italian Sausage Parmigiana</b><span class="lead"></span><span class="price">6.99</span><span class="price">9.99</span></div>
    <div class="row"><b>Italian Sausage &amp; Green Peppers Parmigiana</b><span class="lead"></span><span class="price">6.99</span><span class="price">9.99</span></div>
    <div class="row"><b>Chicken Parmigiana</b><span class="lead"></span><span class="price">6.99</span><span class="price">9.99</span></div>
    <div class="row"><b>Veal Parmigiana</b><span class="lead"></span><span class="price">6.99</span><span class="price">9.99</span></div>
    <div class="row"><b>Eggplant Parmigiana</b><span class="lead"></span><span class="price">6.99</span><span class="price">9.99</span></div>
    <div class="row"><b>GYRO Sandwich on Pita Bread (Chicken or Beef)</b><span class="lead"></span><span class="price">6.99</span><span class="price">9.99</span></div>
    <div class="row"><b>Additional on subs: mushroom, green peppers</b><span class="lead"></span><span class="price">6.99</span><span class="price">9.99</span></div>
    <div class="row"><b>extra meat</b><span class="lead"></span><span class="price">6.99</span><span class="price">9.99</span></div>
    <div class="row"><b>cheese</b><span class="lead"></span><span class="price">6.99</span><span class="price">9.99</span></div>
  </section>

  <!-- Right panel -->
  <section class="panel mid">
    <h2 class="heading">PIZZA</h2>
    <div class="pz-head"><span class="blank"></span><span>7" Mini</span><span>10" S</span><span>13" M</span><span>16" L</span></div>
    <div class="pz"><div class="n"><b>Plain</b><i>(cheese)</i><span class="lead"></span></div><span>4.99</span><span>6.99</span><span>9.49</span><span>10.99</span></div>
    <div class="pz"><div class="n"><b>Pepperoni</b><span class="lead"></span></div><span>4.99</span><span>7.99</span><span>10.49</span><span>12.99</span></div>
    <div class="pz"><div class="n"><b>Sausage</b><span class="lead"></span></div><span>4.99</span><span>7.99</span><span>10.49</span><span>12.99</span></div>
    <div class="pz"><div class="n"><b>Hawaiian Pineapple</b><span class="lead"></span></div><span>4.99</span><span>7.99</span><span>10.49</span><span>12.99</span></div>
    <div class="pz"><div class="n"><b>Meatball</b><span class="lead"></span></div><span>4.99</span><span>7.99</span><span>10.49</span><span>12.99</span></div>
    <div class="pz"><div class="n"><b>Ham</b><span class="lead"></span></div><span>4.99</span><span>7.99</span><span>10.49</span><span>12.99</span></div>
    <div class="pz"><div class="n"><b>Ground Beef</b><span class="lead"></span></div><span>4.99</span><span>7.99</span><span>10.49</span><span>12.99</span></div>
    <div class="pz"><div class="n"><b>Green Peppers</b><span class="lead"></span></div><span>4.99</span><span>7.99</span><span>10.49</span><span>12.99</span></div>
    <div class="pz"><div class="n"><b>Onion</b><span class="lead"></span></div><span>4.99</span><span>7.99</span><span>10.49</span><span>12.99</span></div>
    <div class="pz"><div class="n"><b>Black Olives</b><span class="lead"></span></div><span>4.99</span><span>7.99</span><span>10.49</span><span>12.99</span></div>
    <div class="pz"><div class="n"><b>Mushroom</b><span class="lead"></span></div><span>4.99</span><span>7.99</span><span>10.49</span><span>12.99</span></div>
    <div class="pz"><div class="n"><b>Bacon</b><span class="lead"></span></div><span>4.99</span><span>7.99</span><span>10.49</span><span>12.99</span></div>
    <div class="pz"><div class="n"><b>Anchovies</b><span class="lead"></span></div><span>4.99</span><span>7.99</span><span>10.49</span><span>12.99</span></div>
    <div class="pz"><div class="n"><b>Salami</b><span class="lead"></span></div><span>4.99</span><span>7.99</span><span>10.49</span><span>12.99</span></div>
    <div class="pz pz--wide"><div class="n"><b>Pepperoni, Mushroom, Sausage, Onion</b><span class="lead"></span></div><span>10.49</span><span>13.99</span><span>17.99</span></div>
    <div class="pz"><div class="n"><b>Mama Mia Delight</b><span class="lead"></span></div><span>8.25</span><span>13.25</span><span>16.95</span><span>19.99</span></div>
    <p class="pz-note">(pepperoni, mushroom, sausage, onion, ham, salami, green pepper, meatball)</p>
    <div class="pz"><div class="n"><b>White Pizza</b><i>(w/ Butter &amp; Garlic)</i><span class="lead"></span></div><span>4.99</span><span>7.99</span><span>10.49</span><span>12.99</span></div>
    <div class="pz"><div class="n"><b>Extra Topping</b><span class="lead"></span></div><span>0.99</span><span>1.89</span><span>1.99</span><span>2.20</span></div>

    <h2 class="heading">SANDWICH PLATTERS</h2>
    <div class="row"><b>Fresh Roast Beef on Jumbo Bun w/FF &amp; med. Drink</b><span class="lead"></span><span class="price">8.99</span></div>
    <div class="row"><b>*1/2 lb. Cheeseburger w/ FF &amp; med. Drink</b><span class="lead"></span><span class="price">8.99</span></div>
    <div class="row"><b>BBQ Special on Jumbo Bun w/FF, cole slaw &amp; med. Drink</b><span class="lead"></span><span class="price">8.99</span></div>
    <div class="row"><b>Fish Filet on Sesame Bun w/FF, med. Drink</b><span class="lead"></span><span class="price">8.99</span></div>
    <div class="row"><b>Crab Cake on Sesame Bun w/FF &amp; med. Drink</b><span class="lead"></span><span class="price">8.99</span></div>
    <div class="row"><b>Gyro Sandwich (Beef or Chicken) w/FF &amp; med. Drink</b><span class="lead"></span><span class="price">8.99</span></div>

    <h2 class="heading">SANDWICHES</h2>
    <div class="two-col">
      <div class="list">
        <div class="row"><b>Served on Sesame Bun</b><span class="lead"></span><span class="price">4.99</span></div>
        <div class="row"><b>Roast Beef w/ LTM</b><span class="lead"></span><span class="price">4.99</span></div>
        <div class="row"><b>Tuna Salad</b><span class="lead"></span><span class="price">4.99</span></div>
        <div class="row"><b>Bar-B-Que w/ Cole Slaw</b><span class="lead"></span><span class="price">4.99</span></div>
        <div class="row"><b>Grilled Chicken Breast</b><span class="lead"></span><span class="price">4.99</span></div>
        <div class="row"><b>*Cheeseburger</b><span class="lead"></span><span class="price">3.75</span></div>
      </div>
      <div class="photo grill-photo" role="img" aria-label="Photo of grilled chicken breast with roasted vegetables"></div>
    </div>
  </section>
</main>

</body>
</html>
```